Spa Resort Website

UPDATE:
Note that for the home page we are intending to have a slideshow showcasing elements of the resort, as per:
* www.brackenwellpools.co.nz
* www.velanira.com
* www.wanderlofty-journeys.com
We also need to know how you intend to use the colours to denote subsections, as per the brief below.
Also...the sliders denoting Elegant vs Bold etc seem to have lost their settings. I have reset them to how I believe we set them a couple of weeks ago, but there may be minor differences.
=============================================
We are developing a website for Taupo Kelmarsh, a resort in Taupo, New Zealand.
While we have been provided with a site layout and basic colour scheme, the implementation of this design does not meet the client's needs for a modern, inviting looking site.
We require a designer to work within the outline structure of the site and provide design elements to lift the design. We envisage that these design elements would include styling of the menus, building of the colour schemes from the base colours, home page design.
If you are unsure of the parameters please post a question indicating elements you would like to change and we can comment on feasibility.
We have attached the original design concept and some of the wire framing that we developed from that.
The site has four major sections, each requiring its own, subtly different, colour scheme - these schemes are to be based on the colours in the client's logo (attached). Obviously there does need to be consistency in the colour schemes across the site. The colours from the logo apply as follows:
* Stay (accommodation) - "Orange"
* Soak (Hot Springs and water park) - "Green"
* Soothe (Spa Resort) - "Beige"
* Savour (Summary of experience) - "Choc Brown"
We require the design for 2 pages:
* Home
* Detail Page (eg Family Accommodation)
Design must be flexible in that if we decide at a later date to add another block to the RH area (for example) we are able to while maintaining the integrity of the design.
Menu items include dropdowns.
We are not happy with the current layout of the HOME page and require a full redesign of this.
The resort is 5 star, but also offers camping facilities. The design therefore needs to reflect the high quality of the resort, while also being accessible to those on a budget.
The following sites can be considered reference sites for the look and feel we are seeking:
* www.brackenwellpools.co.nz
* www.velanira.com
Final deliverable is preferred in layered PNG, but .eps is acceptable. .ai is not acceptable.

```html
<!DOCTYPE html>
<html lang="en">
<head>
<meta charset="utf-8">
<title>Taupo Kelmarsh Spa Resort</title>
<link href="https://fonts.googleapis.com/css2?family=Arimo:wght@400;700&family=Roboto+Condensed:wght@700&display=swap" rel="stylesheet">
<style>
:root{
  --page-bg:#efece3;
  --rule-brown:#857761;
  --text:#222;
  --green:#3a9a6a;
  --green-link:#1f9a5a;
  --orange-hi:#f5a54a;
  --nav-top:#ddd2c0;
  --nav-bottom:#b8a487;
  --menu-top:#7b6a3c;
  --menu-bottom:#5a4519;
  --book-top:#ee8a3a;
  --book-bottom:#cf5a10;
  --deals-top:#35b07a;
  --deals-bottom:#0f7f48;
  --panel-top:#b6a68a;
  --panel-bottom:#9b8a6c;
}
*{box-sizing:border-box;margin:0;padding:0}
html,body{width:1200px;height:844px;overflow:hidden;background:var(--page-bg)}
body{font-family:"Arimo",Arial,sans-serif;color:var(--text)}
.stage{position:relative;width:1280px;height:900px;transform:scale(.9375);transform-origin:0 0;
  background:linear-gradient(#fff 0,#fff 150px,var(--page-bg) 240px)}
.stage>*{position:absolute}
.top-rule{left:0;top:0;width:1280px;height:3px;background:var(--rule-brown)}
.brand{left:176px;top:70px;display:flex;align-items:center;gap:10px;font-size:27px;font-weight:700;color:#2b2b2b}
.brand-dot{width:22px;height:22px;border-radius:50%;background:#e0731c}
.contact{right:160px;top:48px;text-align:right}
.contact small{display:block;font-size:13px;color:#333}
.contact strong{display:block;font-size:23px;color:#333;margin-top:2px}
.main-nav{left:402px;top:122px;width:718px;height:41px;display:flex;border-radius:4px 4px 0 0;
  background:linear-gradient(var(--nav-top),var(--nav-bottom))}
.main-nav a{display:flex;align-items:center;justify-content:center;gap:4px;font-size:16px;color:#333;text-decoration:none;border-right:1px solid #a08e72;box-shadow:1px 0 0 #e8dfd0}
.main-nav a:last-child{border:0;box-shadow:none}
.caret{width:0;height:0;border-left:5px solid transparent;border-right:5px solid transparent;border-top:5px solid #333}
.banner-frame{left:160px;top:163px;width:960px;height:75px;background:#fff}
.banner{position:absolute;left:10px;top:10px;width:940px;height:55px;display:flex;align-items:center;padding-left:9px;
  font-size:18px;font-weight:700;color:#111;
  background:linear-gradient(90deg,#e3f0b0 0,#cfe690 25%,#8fc63a 45%,#b6dd4c 62%,#5d9a16 78%,#a4d23a 88%,#3c6e0a 95%,#8cc43a 100%)}
.content{left:160px;top:258px;width:716px;height:660px;border:2px solid #fff;box-shadow:0 0 3px rgba(0,0,0,.12);
  background:linear-gradient(#ecebe6,#fff 180px);padding:0 18px}
.content p.lede{font-size:12.2px;line-height:20px;color:#222;margin-top:22px;width:676px}
.content p.lede+p.lede{margin-top:20px}
.photo-row{display:flex;gap:4px;margin-top:20px}
.photo{height:110px}
.quote{display:flex;gap:12px;margin-top:24px}
.quote-mark{width:44px;height:80px;background:#ece8dd;border-radius:22px 4px 4px 4px;flex:none}
.quote blockquote{font-size:12.2px;line-height:20px;color:#222}
.quote cite{display:block;font-style:normal;font-weight:700;margin-top:10px}
.dotted{border-top:1px dotted #999;margin-top:16px}
.section-title{font-size:22px;font-weight:400;color:#333;margin-top:14px}
.deals{display:flex;margin-top:10px}
.deal{width:349px}
.deal h3{font-size:17px;font-weight:400;color:var(--green)}
.deal .price{font-size:13.5px;font-weight:700;margin-top:10px;color:#222}
.read-more{font-size:12px;font-weight:700;color:var(--green-link);text-decoration:none;display:inline-block}
.deal .read-more{margin-top:8px}
.family-title{font-size:18px;color:#333;margin-top:18px;font-weight:400}
.family{display:flex;gap:24px;margin-top:14px}
.family .photo{width:162px;height:40px}
.family p{font-size:12.2px;line-height:20px}
.side-menu{left:895px;top:258px;width:225px;height:275px;border-radius:4px;border:1px solid #4a380e;
  background:linear-gradient(var(--menu-top),var(--menu-bottom));padding:17px 13px 0}
.side-menu a{display:flex;align-items:center;gap:8px;height:24px;font-size:14px;color:#fff;text-decoration:none;
  border-bottom:1px dotted #a59566;padding-left:7px}
.side-menu a:last-child{border:0}
.side-menu a.current{color:var(--orange-hi)}
.side-menu svg{flex:none}
.cta{left:895px;width:226px;height:46px;border-radius:3px;display:flex;align-items:center;justify-content:center;
  font-family:"Roboto Condensed","Arial Narrow",sans-serif;font-weight:700;font-size:21px;color:#fff;text-shadow:1px 1px 1px rgba(0,0,0,.45)}
.cta.book{top:538px;background:linear-gradient(var(--book-top),var(--book-bottom))}
.cta.specials{top:588px;background:linear-gradient(var(--deals-top),var(--deals-bottom))}
.panel-head{left:895px;width:225px;height:34px;padding-left:15px;display:flex;align-items:center;
  font-family:"Roboto Condensed","Arial Narrow",sans-serif;font-weight:700;font-size:18px;color:#fff;
  background:linear-gradient(var(--panel-top),var(--panel-bottom));border-radius:3px 3px 0 0}
.panel-body{left:895px;width:225px;background:#fff;padding:10px 10px 10px 16px}
.testimonial-head{top:640px}
.testimonial{top:674px;height:132px;overflow:hidden}
.testimonial p{font-size:13.6px;line-height:24px;color:#333;white-space:nowrap}
.testimonial strong{display:block;font-size:13.5px;margin-top:8px;line-height:18px}
.testimonial .dotted{margin:12px 6px 0 -6px}
.testimonial .read-more{display:block;text-align:right;margin:6px 6px 0 0;line-height:16px}
.keep-head{top:812px}
.keep{top:846px;height:60px;padding-right:6px}
.keep p{font-size:12.2px;line-height:20px;color:#222;margin-top:-2px;white-space:nowrap}
</style>
</head>
<body>
<div class="stage">
  <div class="top-rule"></div>

  <div class="brand"><span class="brand-dot"></span>Taupo Kelmarsh</div>

  <div class="contact">
    <small>For More Information</small>
    <strong>+64 7 555 0142</strong>
  </div>

  <nav class="main-nav">
    <a style="width:90px">Home</a>
    <a style="width:110px">Facilities<span class="caret"></span></a>
    <a style="width:95px">Deals<span class="caret"></span></a>
    <a style="width:94px">About<span class="caret"></span></a>
    <a style="width:101px">Gallery<span class="caret"></span></a>
    <a style="width:96px">Taupo<span class="caret"></span></a>
    <a style="width:132px">Contact Us</a>
  </nav>

  <div class="banner-frame">
    <div class="banner" role="img" aria-label="Soft green foliage banner">Stay at Taupo Kelmarsh Spa Resort</div>
  </div>

  <main class="content">
    <p class="lede">Lorem ipsum onsectetuer adipiscing elit, sed diam nonummy nibh euismod tincidunt ut laoreet dolore magna aliquam erat volutpat. Ut wisi enim ad minim veniam, quis nostrud exerci tation ullamcorper suscipit lobortis nisl ut aliquip ex ea commodo consequat.</p>
    <p class="lede">Lorem ipsum onsectetuer adipiscing elit, sed diam nonummy nibh euismod tincidunt ut laoreet dolore magna aliquam erat volutpat. Ut wisi enim ad minim veniam, quis nostrud exerci tation ullamcorper suscipit lobortis nisl ut aliquip ex ea commodo consequat.</p>

    <div class="photo-row">
      <div class="photo" style="width:220px;background:linear-gradient(135deg,#f4f4f2,#d9d6d0 60%,#6b6560)" role="img" aria-label="Motel lounge with sofa and bedroom beyond"></div>
      <div class="photo" style="width:228px;background:linear-gradient(170deg,#d8d2c8,#e9e4da 45%,#d9644a 75%,#c7bfae)" role="img" aria-label="Made bed with coral throw and cushions"></div>
      <div class="photo" style="width:220px;background:linear-gradient(180deg,#f5f5f3,#e2e2df 60%,#4a4a4a)" role="img" aria-label="Dining table and kitchenette"></div>
    </div>

    <div class="quote">
      <div class="quote-mark"></div>
      <blockquote>Lorem ipsum onsectetuer adipiscing elit, sed diam nonummy nibh euismod tincidunt ut laoreet dolore magna aliquam erat volutpat. Ut wisi enim ad minim veniam, quis nostrud exerci tation ullamcorper suscipit lobortis nisl ut aliquip ex ea commodo consequat.
        <cite>— Marisol - USA</cite>
      </blockquote>
    </div>

    <div class="dotted"></div>
    <h2 class="section-title">Deals</h2>
    <div class="deals">
      <div class="deal">
        <h3>Kelmarsh Breakaway for 2 people</h3>
        <p class="price">$149 per night for 2 people ( extra person $20)</p>
        <a class="read-more">Read more...</a>
      </div>
      <div class="deal">
        <h3>Romantic Getaway for 2 people</h3>
        <p class="price">$149 per night for 2 people ( extra person $20)</p>
        <a class="read-more">Read more...</a>
      </div>
    </div>
    <div class="dotted" style="margin-top:22px"></div>

    <h2 class="family-title">Family Accommodation</h2>
    <div class="family">
      <div class="photo" style="background:linear-gradient(#7ea7c9,#9bb98a)" role="img" aria-label="Family unit exterior"></div>
      <p>Lorem ipsum onsectetuer adipiscing elit, sed diam nonummy nibh euismod tincidunt ut</p>
    </div>
  </main>

  <nav class="side-menu">
    <a><svg width="12" height="8" viewBox="0 0 12 8"><path d="M0 4h10M7 1l3 3-3 3" stroke="#e8d9a8" fill="none" stroke-width="1.3"/></svg>Holiday Park</a>
    <a><svg width="12" height="8" viewBox="0 0 12 8"><path d="M0 4h10M7 1l3 3-3 3" stroke="#e8d9a8" fill="none" stroke-width="1.3"/></svg>Family Accommodation</a>
    <a><svg width="12" height="8" viewBox="0 0 12 8"><path d="M0 4h10M7 1l3 3-3 3" stroke="#e8d9a8" fill="none" stroke-width="1.3"/></svg>Luxury Accommodation</a>
    <a><svg width="12" height="8" viewBox="0 0 12 8"><path d="M0 4h10M7 1l3 3-3 3" stroke="#e8d9a8" fill="none" stroke-width="1.3"/></svg>Spa Chalets</a>
    <a class="current"><svg width="12" height="8" viewBox="0 0 12 8"><path d="M0 4h10M7 1l3 3-3 3" stroke="#e8d9a8" fill="none" stroke-width="1.3"/></svg>Motels</a>
    <a><svg width="12" height="8" viewBox="0 0 12 8"><path d="M0 4h10M7 1l3 3-3 3" stroke="#e8d9a8" fill="none" stroke-width="1.3"/></svg>Cabins</a>
    <a><svg width="12" height="8" viewBox="0 0 12 8"><path d="M0 4h10M7 1l3 3-3 3" stroke="#e8d9a8" fill="none" stroke-width="1.3"/></svg>Luxury Lodges</a>
    <a><svg width="12" height="8" viewBox="0 0 12 8"><path d="M0 4h10M7 1l3 3-3 3" stroke="#e8d9a8" fill="none" stroke-width="1.3"/></svg>Campsites</a>
    <a><svg width="12" height="8" viewBox="0 0 12 8"><path d="M0 4h10M7 1l3 3-3 3" stroke="#e8d9a8" fill="none" stroke-width="1.3"/></svg>Motorhomes</a>
    <a><svg width="12" height="8" viewBox="0 0 12 8"><path d="M0 4h10M7 1l3 3-3 3" stroke="#e8d9a8" fill="none" stroke-width="1.3"/></svg>Facilities</a>
  </nav>

  <a class="cta book">Book And Pay Online</a>
  <a class="cta specials">Great Deals &amp; Specials</a>

  <div class="panel-head testimonial-head">TESTIMONIALS</div>
  <div class="panel-body testimonial">
    <p>... We haven't stayed anywhere<br>else in the last five years.</p>
    <strong>Rowan, NZ</strong>
    <div class="dotted"></div>
    <a class="read-more">Read more...</a>
  </div>

  <div class="panel-head keep-head">KEEP IN TOUCH</div>
  <div class="panel-body keep">
    <p>Keep up to date with what's<br>happening in Taupo and at Kelmarsh</p>
  </div>
</div>
</body>
</html>
```